varnok llc

excavating and landscaping

Target Market(s)

Industry/Entity Type

Contact Information for Business Card

file atach

Font styles to use
Serif

```html
<!DOCTYPE html>
<html lang="en">
<head>
<meta charset="utf-8">
<title>Varnok LLC — Business Card</title>
<link rel="stylesheet" href="https://fonts.googleapis.com/css2?family=Orbitron:wght@600;700;800&display=swap">
<style>
  :root {
    --backdrop: #ababab;
    --card-white: #ffffff;
    --ink: #111111;
    --accent-red: #c40c0c;
    --faint-grey: #d6d6d6;
    --night-1: #141312;
    --night-2: #2a2620;
    --night-3: #3a3323;
    --logo-white: #f2f2f2;
  }
  * { margin: 0; padding: 0; box-sizing: border-box; }
  html, body {
    width: 1200px; height: 1000px; overflow: hidden;
    background: var(--backdrop);
    font-family: "Orbitron", sans-serif;
  }
  .canvas { position: relative; width: 1200px; height: 1000px; }
  .card {
    position: absolute; left: 294px; width: 613px; height: 352px;
    border-radius: 22px; overflow: hidden;
  }
  .card--front { top: 93px; background: var(--card-white); }
  .card--back { top: 547px; }

  .front__brand {
    position: absolute; left: 340px; top: 0;
  }
  .front__brand-name {
    position: absolute; left: 46px; top: 30px;
    font-size: 20px; font-weight: 800; letter-spacing: 1px;
    color: var(--faint-grey); white-space: nowrap;
  }
  .front__person {
    position: absolute; left: 44px; top: 133px;
    font-size: 25px; font-weight: 700; letter-spacing: 1px;
    color: var(--ink);
  }
  .contact {
    position: absolute; left: 44px; display: flex; align-items: center; gap: 9px;
    font-size: 16px; font-weight: 700; letter-spacing: 0.5px; color: var(--ink);
  }
  .contact--phone { top: 184px; }
  .contact--place { top: 224px; }
  .contact__icon { width: 25px; height: 25px; flex: none; }

  .back__scene {
    position: absolute; inset: 0;
    background:
      radial-gradient(ellipse at 12% 55%, var(--night-3) 0%, transparent 35%),
      radial-gradient(ellipse at 90% 55%, var(--night-3) 0%, transparent 30%),
      linear-gradient(180deg, var(--night-2) 0%, var(--night-1) 100%);
  }
  .back__brand {
    position: absolute; left: 0; right: 0; top: 205px;
    display: flex; justify-content: center; align-items: center; gap: 16px;
  }
  .back__brand-mark { width: 26px; height: 26px; background: var(--accent-red); }
  .back__brand-name {
    font-size: 52px; font-weight: 800; letter-spacing: 2px;
    color: var(--logo-white); white-space: nowrap;
  }
</style>
</head>
<body>
<main class="canvas">
  <section class="card card--front">
    <p class="front__brand-name">VARNOK LLC</p>
    <h1 class="front__person">DALE MERCER</h1>
    <p class="contact contact--phone">
      <svg class="contact__icon" viewBox="0 0 24 24" aria-hidden="true">
        <circle cx="12" cy="12" r="12" fill="var(--accent-red)"/>
        <path d="M8.2 5.8c.5-.3 1.1-.2 1.4.3l1.2 2c.3.5.2 1-.2 1.3l-.9.7c.6 1.3 1.7 2.5 3 3.1l.7-.9c.3-.4.9-.5 1.3-.2l2 1.2c.5.3.6.9.3 1.4l-.7 1.1c-.5.7-1.4 1-2.2.7-3.2-1.1-5.7-3.6-6.8-6.8-.3-.8 0-1.7.7-2.2z" fill="#fff"/>
      </svg>
      <span>(555) 014-2287</span>
    </p>
    <p class="contact contact--place">
      <svg class="contact__icon" viewBox="0 0 24 24" aria-hidden="true">
        <circle cx="12" cy="12" r="12" fill="var(--accent-red)"/>
        <path d="M12 4.5a5 5 0 0 0-5 5c0 3.7 5 9.5 5 9.5s5-5.8 5-9.5a5 5 0 0 0-5-5z" fill="#fff"/>
        <circle cx="12" cy="9.6" r="2" fill="var(--accent-red)"/>
      </svg>
      <span>Brookhaven | CA 95000</span>
    </p>
  </section>

  <section class="card card--back">
    <div class="back__scene" role="img" aria-label="Dark, blurred photo of a construction site with yellow excavators in front of a building"></div>
    <div class="back__brand">
      <span class="back__brand-mark"></span>
      <span class="back__brand-name">VARNOK LLC</span>
    </div>
  </section>
</main>
</body>
</html>
```